Vitamin B12 Liquid Drops Label

hi, i need a label designed for my vitamin b12 drops that i am going to be selling on bazaarly. the label needs to quickly capture the attention of a buyer as he or she is scrolling through the thumbnail search results on bazaarly.net my brand is called zulmo. i already have an example brand logo i will be using, however, i need help designing the rest of the label. attached are some examples of labels i like for other supplements.some of these examples are pink. i do not want pink. please go for a blue/green color scheme. THE DESIGN MUST BE BOLD

Target Market(s)

adults ages 30 - 64

Font styles to use
Sans Serif

Colors
0455a3
cedeed
3176b5
85acd3
cfdeed
9bcb3b
abd037
cadf82
00a990

Requirements
Must have
• - bold design
• - somewhat gender-neutral color scheme because this will be used equally by men and women
• - B12 MUST be very prominent and visible on the label
Should not have
• - it should not be "crunchy" looking

```html
<!DOCTYPE html>
<html lang="en">
<head>
<meta charset="utf-8">
<title>Zulmo Vitamin B12 – Label Variants</title>
<link rel="stylesheet" href="https://fonts.googleapis.com/css2?family=Jost:wght@300;400;800&family=Ultra&display=swap">
<style>
  :root {
    --canvas: #ffffff;
    --label-blue: #2fa9dd;
    --band-navy: #14204a;
    --band-teal: #3f8fb8;
    --rule-white: #ffffff;
    --ink-black: #111111;
    --ink-navy: #1d3a6e;
    --accent-lime: #d6d95a;
    --accent-ice: #cfe3f3;
  }
  * { box-sizing: border-box; margin: 0; padding: 0; }
  html, body {
    width: 1200px; height: 764px; overflow: hidden;
    background: var(--canvas);
  }
  .stage { position: relative; width: 1200px; height: 764px; }
  .label {
    position: absolute; top: 302px;
    width: 240px; height: 292px;
    background: var(--label-blue);
    font-family: "Jost", sans-serif;
    color: #fff;
  }
  .label--lime { left: 236px; --accent: var(--accent-lime); }
  .label--ice  { left: 694px; --accent: var(--accent-ice); }
  .brand {
    position: absolute; top: 22px; left: 0; right: 0;
    text-align: center;
    font-weight: 800; font-size: 34px; letter-spacing: 1px; line-height: 1;
  }
  .rule {
    position: absolute; left: 0; right: 0; height: 2px;
    background: var(--rule-white);
  }
  .rule--top { top: 86px; }
  .rule--bottom { top: 190px; }
  .pattern-band {
    position: absolute; top: 92px; left: 0; right: 0; height: 94px;
    background: linear-gradient(90deg, var(--band-navy), var(--band-teal) 50%, var(--band-navy));
  }
  .vitamin-badge {
    position: absolute; left: 50%; top: 139px;
    width: 130px; height: 130px; margin: -65px 0 0 -65px;
    border-radius: 50%;
    background: var(--accent);
    border: 2px solid var(--rule-white);
    display: flex; align-items: center; justify-content: center;
    color: var(--ink-black); line-height: 1;
  }
  .vitamin-badge .letter { font-family: "Ultra", serif; font-size: 58px; }
  .vitamin-badge .number { font-family: "Jost", sans-serif; font-weight: 300; font-size: 42px; margin-left: 1px; margin-top: 6px; letter-spacing: -2px; }
  .product-type {
    position: absolute; top: 210px; left: 0; right: 0;
    text-align: center;
    font-weight: 300; font-size: 27px; letter-spacing: 1px; line-height: 1;
  }
  .dose-tag {
    position: absolute; top: 264px; left: 50%;
    transform: translateX(-50%);
    background: var(--accent);
    color: var(--ink-navy);
    padding: 2px 9px;
    font-weight: 400; font-size: 10.5px; line-height: 1.15;
    text-align: center; white-space: nowrap;
  }
  .label--ice .dose-tag { color: var(--ink-black); }
</style>
</head>
<body>
<main class="stage">
  <section class="label label--lime">
    <h1 class="brand">ZULMO</h1>
    <div class="rule rule--top"></div>
    <div class="pattern-band" role="img" aria-label="Decorative navy and teal line pattern band"></div>
    <div class="rule rule--bottom"></div>
    <div class="vitamin-badge"><span class="letter">B</span><span class="number">12</span></div>
    <p class="product-type">VITAMIN</p>
    <p class="dose-tag">1000 MCG<br>45 TABLETS</p>
  </section>

  <section class="label label--ice">
    <h1 class="brand">ZULMO</h1>
    <div class="rule rule--top"></div>
    <div class="pattern-band" role="img" aria-label="Decorative navy and teal line pattern band"></div>
    <div class="rule rule--bottom"></div>
    <div class="vitamin-badge"><span class="letter">B</span><span class="number">12</span></div>
    <p class="product-type">VITAMIN</p>
    <p class="dose-tag">1000 MCG<br>45 TABLETS</p>
  </section>
</main>
</body>
</html>
```